Redesign existing website to have updated look and content

have existing website but do not have the time to put page detail that I want into it. we are a residential, family owned and operated HVAC and plumbing company. we offer service, repair, replacement, maintenance, new installations. the owner has over 20 years experience. got into his own business bc of high pricing charged by old employer. we believe CUSTOMER SERVICE IS THE ONLY THING THAT MATTERS, we are an harlow's guide top trade award winner. we just recently were invited to sell on Brindlemart. we currently have the owner and 1 other tech and a helper in the field. we want to keep small so that service doesn't suffer

Target Market(s)

homeowners over 28 in the Bucks and Montgomery and Delawre Counties of PA

Industry/Entity Type

Hvac

Number of Pages Required

4 page

Font styles to use
Serif
Sans Serif
Decorative

Colors
0255a3
ec1f27

Requirements
Must have
• more content and information
• online scheduling thru V Cita
• information that is not related to HVAC that can be updated daily
Nice to have
• apps that customers will be drawn to website with
• information regarding our services and costs
• online scheduling
• better content!!!!
• links to vendors and outside information

```html
<!DOCTYPE html>
<html lang="en">
<head>
<meta charset="utf-8">
<title>Keystone Comfort – Heating, Cooling &amp; Plumbing</title>
<link rel="stylesheet" href="https://fonts.googleapis.com/css2?family=Open+Sans:ital,wght@0,400;0,600;0,700;0,800;1,400&display=swap">
<style>
:root{
  --brand-blue:#0255a3;
  --brand-red:#ec1f27;
  --deep-blue:#1f4f91;
  --text:#555c66;
  --muted:#8a9099;
  --band-grey:#ebebeb;
  --peach:#f6c17f;
  --white:#ffffff;
  --line:#dcdcdc;
}
*{box-sizing:border-box;margin:0;padding:0}
html,body{width:1200px;height:2528px;overflow:hidden}
body{font-family:"Open Sans",Arial,sans-serif;color:var(--text);background:var(--white);position:relative}
.abs{position:absolute}

/* header */
.site-header{left:0;top:0;width:1200px;height:112px}
.brand{left:100px;top:26px;display:flex;align-items:center;gap:14px}
.brand-mark{width:54px;height:54px;border-radius:50%;background:var(--brand-red)}
.brand-name{font-size:30px;font-weight:800;color:var(--brand-blue);line-height:1}
.search{left:812px;top:48px;display:flex}
.search-field{width:248px;height:32px;border:1px solid var(--line);font-size:13px;color:var(--muted);padding:6px 10px}
.search-btn{width:36px;height:32px;background:var(--brand-blue);display:flex;align-items:center;justify-content:center}

.main-nav{left:0;top:112px;width:1200px;height:48px;background:var(--deep-blue)}
.main-nav ul{list-style:none;display:flex;height:48px;margin-left:100px}
.main-nav li{font-size:14px;font-weight:600;color:var(--white);padding:0 28px;line-height:48px;text-transform:uppercase}
.main-nav li.active{background:var(--brand-red)}

/* hero */
.hero{left:0;top:160px;width:1200px;height:500px;background:linear-gradient(135deg,#d9cdb9 0%,#b9a487 40%,#8e7a5d 70%,#c4b59c 100%)}
.hero-title{left:0;top:470px;width:1200px;text-align:center;font-size:38px;font-weight:700;color:var(--white);letter-spacing:1px;text-transform:uppercase}
.hero-dots{left:0;top:618px;width:1200px;display:flex;justify-content:center;gap:10px}
.hero-dots span{width:11px;height:11px;border-radius:50%;background:rgba(255,255,255,.6)}
.hero-dots span.on{background:var(--white)}

.section-title{font-size:30px;font-weight:700;color:var(--brand-red);text-transform:uppercase}
.rule{height:2px;background:var(--line)}
.body-copy{font-size:14px;line-height:24px;color:var(--muted)}

/* about */
.about-title{left:100px;top:716px}
.about-rule{left:100px;top:760px;width:580px}
.about-copy{left:100px;top:784px;width:600px}
.about-visual{left:770px;top:720px;width:230px;height:230px;background:linear-gradient(180deg,#c9ccd1,#8d9198)}
.value-badge{left:960px;top:880px;width:80px;height:80px;border-radius:50%;background:var(--brand-red)}

/* services */
.services-title{left:100px;top:1030px}
.services-rule{left:100px;top:1074px;width:1000px}
.service-card{top:1104px;width:240px;height:318px;color:var(--white);text-align:center}
.service-card.red{background:var(--brand-red)}
.service-card.blue{background:var(--deep-blue)}
.service-card h3{font-size:15px;font-weight:700;text-transform:uppercase;margin-top:26px}
.card-icon{width:80px;height:80px;border-radius:50%;background:var(--white);margin:20px auto 0;display:flex;align-items:center;justify-content:center}
.service-card p{font-size:12px;line-height:19px;margin:30px 24px 0}
.read-more{position:absolute;right:20px;bottom:18px;font-size:13px;font-weight:600}
.card-shadow{top:1422px;width:240px;height:10px;background:linear-gradient(180deg,rgba(0,0,0,.18),rgba(0,0,0,0))}

/* scheduling */
.schedule-band{left:0;top:1500px;width:1200px;height:340px;background:var(--band-grey)}
.schedule-title{left:100px;top:1568px;font-size:26px}
.schedule-copy{left:100px;top:1618px;width:560px}
.connect-btn{left:100px;top:1762px;width:182px;height:34px;background:var(--brand-blue);color:var(--white);font-size:12px;font-weight:700;display:flex;align-items:center;justify-content:center;gap:8px}
.booking-visual{left:720px;top:1556px;width:380px;height:262px;background:linear-gradient(150deg,#5c6168,#2c2f34 60%,#1c1e21)}

/* award + testimonials */
.award-title{left:100px;top:1920px;font-size:26px}
.award-rule{left:100px;top:1960px;width:480px}
.award-box{left:100px;top:1990px;width:480px;height:200px;border:1px solid var(--line);background:var(--white)}
.award-seal{left:126px;top:2020px;width:110px;height:140px;border:1px solid var(--line);display:flex;align-items:center;justify-content:center}
.award-seal span{width:70px;height:70px;border-radius:50%;background:#d9a62a}
.award-text{left:262px;top:2016px;width:296px}
.award-text h4{font-size:14px;font-weight:700;color:#333;margin-bottom:8px;text-transform:uppercase}
.award-text p{font-size:13px;line-height:21px;color:var(--muted)}
.award-text b{color:#333}
.testi-title{left:620px;top:1920px;font-size:26px}
.testi-rule{left:620px;top:1960px;width:480px}
.testi-box{left:600px;top:1980px;width:500px;height:206px;background:var(--peach)}
.testi-photo{left:622px;top:2036px;width:72px;height:72px;border-radius:50%;background:linear-gradient(160deg,#c98f74,#7a4b3a)}
.testi-quote{left:716px;top:2030px;width:300px;font-size:13px;line-height:21px;color:var(--white);font-style:italic}
.testi-name{left:716px;top:2134px;font-size:13px;font-weight:700;color:var(--white)}
.quote-mark{left:1048px;top:1996px;font-size:54px;font-weight:800;color:var(--white);line-height:1}

/* footer */
.site-footer{left:0;top:2254px;width:1200px;height:274px;background:var(--deep-blue);color:var(--white)}
.foot-brand{left:100px;top:2282px;display:flex;align-items:center;gap:10px}
.foot-brand .brand-mark{width:36px;height:36px}
.foot-brand .brand-name{font-size:20px;color:var(--white)}
.foot-small{font-size:11px;line-height:18px;color:#cfdcf0}
.foot-legal{left:100px;top:2334px}
.socials{left:100px;top:2364px;display:flex;gap:8px}
.socials span{width:22px;height:22px;background:rgba(255,255,255,.85)}
.partner{left:100px;top:2400px;width:118px;height:30px;background:var(--white);color:#222;font-size:14px;font-weight:700;display:flex;align-items:center;justify-content:center}
.foot-col h5{font-size:18px;font-weight:700;text-transform:uppercase;margin-bottom:6px}
.foot-col .under{width:170px;height:1px;background:rgba(255,255,255,.4);margin-bottom:12px}
.foot-col ul{list-style:none}
.col-links{left:380px;top:2282px}
.col-contact{left:640px;top:2282px}
.col-locations{left:940px;top:2282px}
.copyright{left:940px;top:2494px}
</style>
</head>
<body>

<header class="abs site-header">
  <div class="abs brand"><span class="brand-mark"></span><span class="brand-name">Keystone Comfort</span></div>
  <div class="abs search">
    <div class="search-field">Search</div>
    <div class="search-btn"><svg width="16" height="16" viewBox="0 0 16 16"><circle cx="6.5" cy="6.5" r="4.5" fill="none" stroke="#fff" stroke-width="2"/><line x1="10" y1="10" x2="14" y2="14" stroke="#fff" stroke-width="2"/></svg></div>
  </div>
</header>

<nav class="abs main-nav">
  <ul>
    <li class="active">Home</li><li>About Us</li><li>Services</li><li>Blog</li><li>Online Scheduling</li><li>Video Testimonials</li><li>Contact Us</li>
  </ul>
</nav>

<section>
  <div class="abs hero" role="img" aria-label="Photo of plumbing tools, wrench and brass fittings on a canvas work glove"></div>
  <h1 class="abs hero-title">Super Service Award Winner</h1>
  <div class="abs hero-dots"><span class="on"></span><span></span><span></span></div>
</section>

<section>
  <h2 class="abs section-title about-title">About Us</h2>
  <div class="abs rule about-rule"></div>
  <p class="abs body-copy about-copy">Family owned and operated since day one, our small team brings over twenty years of heating, cooling and plumbing know-how to homes across Bucks, Montgomery and Delaware Counties. Our owner started this company to offer fair, honest pricing. We stay small on purpose so every visit gets full attention, clear advice and work done right the first time, every time, with a smile.</p>
  <div class="abs about-visual" role="img" aria-label="Photo of a residential furnace unit"></div>
  <div class="abs value-badge" role="img" aria-label="Value badge"></div>
</section>

<section>
  <h2 class="abs section-title services-title">Our Services</h2>
  <div class="abs rule services-rule"></div>

  <article class="abs service-card red" style="left:100px">
    <h3>Repair</h3>
    <div class="card-icon"><svg width="44" height="44" viewBox="0 0 44 44"><path d="M30 6a9 9 0 0 0-8 12L7 33a3 3 0 0 0 4 4l15-15a9 9 0 0 0 12-8l-5 5-5-1-1-5z" fill="var(--brand-red)"/></svg></div>
    <p>Fast, fair fixes for heating, cooling and plumbing trouble.</p>
    <span class="read-more">Read more</span>
  </article>
  <article class="abs service-card blue" style="left:360px">
    <h3>Replacement</h3>
    <div class="card-icon"><svg width="44" height="44" viewBox="0 0 44 44"><path d="M34 16a13 13 0 0 0-24-2M10 28a13 13 0 0 0 24 2" fill="none" stroke="var(--brand-red)" stroke-width="4"/><path d="M6 8v8h8M38 36v-8h-8" fill="none" stroke="var(--brand-red)" stroke-width="4"/></svg></div>
    <p>Efficient new systems sized right for your home and budget.</p>
    <span class="read-more">Read more</span>
  </article>
  <article class="abs service-card red" style="left:620px">
    <h3>Maintenance</h3>
    <div class="card-icon"><svg width="44" height="44" viewBox="0 0 44 44"><circle cx="22" cy="22" r="8" fill="none" stroke="var(--brand-red)" stroke-width="4"/><path d="M22 4v7M22 33v7M4 22h7M33 22h7M9 9l5 5M30 30l5 5M9 35l5-5M30 14l5-5" stroke="var(--brand-red)" stroke-width="4"/></svg></div>
    <p>Seasonal tune-ups that keep your equipment running longer.</p>
    <span class="read-more">Read more</span>
  </article>
  <article class="abs service-card blue" style="left:880px">
    <h3>New Installations</h3>
    <div class="card-icon"><svg width="44" height="44" viewBox="0 0 44 44"><path d="M6 22 22 8l16 14M11 18v18h22V18" fill="none" stroke="var(--brand-red)" stroke-width="4"/><path d="M22 22v10M17 27h10" stroke="var(--brand-red)" stroke-width="4"/></svg></div>
    <p>Complete installs for new comfort and water systems.</p>
    <span class="read-more">Read more</span>
  </article>
  <div class="abs card-shadow" style="left:100px"></div>
  <div class="abs card-shadow" style="left:360px"></div>
  <div class="abs card-shadow" style="left:620px"></div>
  <div class="abs card-shadow" style="left:880px"></div>
</section>

<section>
  <div class="abs schedule-band"></div>
  <h2 class="abs section-title schedule-title">Online Scheduling Easy</h2>
  <p class="abs body-copy schedule-copy">Book your visit online in just a few clicks. Pick a day and time that suits you, tell us what you need, and we will confirm right away. No waiting on hold, no phone tag, just quick and simple scheduling from any device at any hour.</p>
  <div class="abs connect-btn">CLICK TO CONNECT <svg width="12" height="12" viewBox="0 0 12 12"><path d="M3 1l5 5-5 5" fill="none" stroke="#fff" stroke-width="2"/></svg></div>
  <div class="abs booking-visual" role="img" aria-label="Photo of a keyboard with an online booking key"></div>
</section>

<section>
  <h2 class="abs section-title award-title">Super Service Award</h2>
  <div class="abs rule award-rule"></div>
  <div class="abs award-box"></div>
  <div class="abs award-seal" role="img" aria-label="Award seal"><span></span></div>
  <div class="abs award-text">
    <h4>Super Service Award</h4>
    <p>Customers rated our team on the <b>harlow's guide top trade award</b> for friendly service, fair prices and quality work.</p>
  </div>

  <h2 class="abs section-title testi-title">Testimonials</h2>
  <div class="abs testi-box"></div>
  <div class="abs quote-mark">&ldquo;</div>
  <div class="abs testi-photo" role="img" aria-label="Customer portrait"></div>
  <p class="abs testi-quote">Friendly, on time and honest. They explained every option and fixed our furnace the same day. We will never call anyone else.</p>
  <p class="abs testi-name">&mdash; Dana R.</p>
</section>

<footer>
  <div class="abs site-footer"></div>
  <div class="abs foot-brand"><span class="brand-mark"></span><span class="brand-name">Keystone Comfort</span></div>
  <p class="abs foot-small foot-legal">Licensed &amp; insured in PA · Privacy Policy</p>
  <div class="abs socials"><span></span><span></span><span></span><span></span></div>
  <div class="abs partner">Brindlemart</div>

  <div class="abs foot-col col-links">
    <h5>Links</h5><div class="under"></div>
    <ul class="foot-small"><li>Home</li><li>About</li><li>Blog</li><li>Services</li><li>Gallery</li></ul>
  </div>
  <div class="abs foot-col col-contact">
    <h5>Contact Us</h5><div class="under"></div>
    <ul class="foot-small"><li>Telephone: 215 555 0148</li><li>Telephone: 215 555 0192</li><li>Fax: 215 555 0177</li><li>Email: info@keystonecomfort.example</li></ul>
  </div>
  <div class="abs foot-col col-locations">
    <h5>Locations</h5><div class="under"></div>
    <ul class="foot-small"><li>412 Fernway Road</li><li>Doylestown, PA 18901</li><li>Get directions</li></ul>
  </div>
  <p class="abs foot-small copyright">© 2024 Keystone Comfort. All rights reserved.</p>
</footer>

</body>
</html>
```